Tidal Fern Business Cards

We need something new, fun and exciting for business cards. Our current ones are just plain and we need a design that pops. We want name, position held, phone, email on the front, and a 20% discount on the back. I have also uploaded our old business cards creative to see what we are not wanting, and how boring they were and we want something jazzed up from this, cool design and catches people attention.

```html
<!DOCTYPE html>
<html lang="en">
<head>
<meta charset="utf-8">
<title>Tidal Fern Business Cards</title>
<link href="https://fonts.googleapis.com/css2?family=Montserrat:wght@400;500;700;800&display=swap" rel="stylesheet">
<style>
  :root {
    --backdrop: #e0e0e0;
    --card: #ffffff;
    --navy: #1b3d6e;
    --coral: #f3736f;
    --blush: #f9c9ca;
    --blush-deep: #f7b2b3;
  }
  * { box-sizing: border-box; margin: 0; padding: 0; }
  html, body { width: 1200px; height: 1200px; overflow: hidden; }
  body {
    background: var(--backdrop);
    font-family: "Montserrat", sans-serif;
    color: var(--navy);
    position: relative;
  }
  .card {
    position: absolute;
    left: 233px;
    width: 734px;
    height: 401px;
    background: var(--card);
    border-radius: 18px;
    overflow: hidden;
    box-shadow: 0 4px 10px rgba(0,0,0,0.45);
  }
  .card-front { top: 135px; }
  .card-back { top: 660px; }

  .decor {
    position: absolute;
    border-radius: 46% 54% 50% 50%;
  }
  .card-front .decor {
    left: -40px; top: -30px; width: 400px; height: 400px;
    background: radial-gradient(circle at 45% 45%, var(--blush) 0%, rgba(249,201,202,0.85) 60%, rgba(249,201,202,0) 72%);
  }
  .card-back .decor {
    left: 360px; top: 40px; width: 420px; height: 400px;
    background: radial-gradient(circle at 55% 50%, var(--blush-deep) 0%, rgba(247,178,179,0.85) 60%, rgba(247,178,179,0) 72%);
  }

  .brand {
    position: absolute;
    display: flex;
    align-items: center;
    gap: 12px;
  }
  .brand-dot {
    width: 34px; height: 34px;
    border-radius: 50%;
    background: var(--coral);
  }
  .brand-name {
    font-weight: 700;
    font-size: 56px;
    letter-spacing: -1px;
    line-height: 1;
    color: var(--navy);
  }
  .card-front .brand { left: 220px; top: 30px; }
  .tagline {
    position: absolute;
    left: 260px; top: 98px;
    font-weight: 800;
    font-size: 15px;
    letter-spacing: 2px;
  }
  .contact-icons {
    position: absolute;
    left: 263px; top: 128px;
  }
  .details {
    position: absolute;
    left: 0; right: 0; top: 158px;
    text-align: center;
    transform: translateX(4px);
    font-size: 37px;
    line-height: 52px;
  }

  .motto-badge {
    position: absolute;
    left: 75px; top: 73px;
    overflow: visible;
  }
  .card-back .brand-name.plain {
    position: absolute;
    left: 76px; top: 266px;
    font-size: 52px;
  }
  .offer {
    position: absolute;
    left: 441px; top: 100px;
    width: 233px; height: 204px;
    border: 2.5px solid var(--navy);
    border-radius: 24px;
    text-align: center;
    padding-top: 38px;
  }
  .offer-rate {
    font-weight: 500;
    font-size: 84px;
    line-height: 0.9;
    letter-spacing: -3px;
  }
  .offer-label {
    font-weight: 400;
    font-size: 47px;
    line-height: 1;
    letter-spacing: -2px;
  }
</style>
</head>
<body>

<section class="card card-front">
  <div class="decor" role="img" aria-label="Large soft pink brand decoration"></div>
  <div class="brand">
    <span class="brand-dot"></span>
    <span class="brand-name">Tidal Fern</span>
  </div>
  <p class="tagline">CANNABIS DISPENSARY</p>
  <svg class="contact-icons" width="220" height="30" viewBox="0 0 220 30" fill="none" stroke="#1b3d6e" stroke-width="1.5" stroke-linecap="round" stroke-linejoin="round">
    <line x1="0" y1="15" x2="52" y2="15"/>
    <line x1="158" y1="15" x2="210" y2="15"/>
    <path d="M63 8c-2 2-2 5 1 9s7 6 9 5l2-2-3-3-2 1c-2-1-3-3-4-4l1-2-3-3z"/>
    <path d="M70 6a6 6 0 0 1 5 5M70 2a10 10 0 0 1 9 9"/>
    <path d="M105 28c-5-8-8-12-8-16a8 8 0 0 1 16 0c0 4-3 8-8 16z"/>
    <circle cx="105" cy="11" r="3"/>
    <ellipse cx="105" cy="28" rx="4" ry="1.2"/>
    <path d="M127 13l11-7 11 7v11h-22z"/>
    <path d="M127 13l11 7 11-7"/>
    <line x1="133" y1="12" x2="143" y2="12"/>
    <line x1="133" y1="15" x2="143" y2="15"/>
  </svg>
  <div class="details">
    <p>phone</p>
    <p>position held</p>
    <p>E mail</p>
  </div>
</section>

<section class="card card-back">
  <div class="decor" role="img" aria-label="Large soft pink brand decoration"></div>
  <svg class="motto-badge" width="260" height="190" viewBox="0 0 260 190">
    <defs>
      <path id="motto-arc" d="M36 152 A100 100 0 1 1 224 152"/>
    </defs>
    <text font-family="Montserrat, sans-serif" font-weight="700" font-size="22" fill="#1b3d6e" letter-spacing="8">
      <textPath href="#motto-arc" startOffset="50%" text-anchor="middle">STAY CALM, GROW</textPath>
    </text>
    <circle cx="130" cy="118" r="22" fill="#f3736f"/>
  </svg>
  <span class="brand-name plain">Tidal Fern</span>
  <div class="offer">
    <p class="offer-rate">20%</p>
    <p class="offer-label">Discount</p>
  </div>
</section>

</body>
</html>
```